Webshop facelift - modern, sales oriented, mobile first

We need facelifted webshop, which is running for few years.
www.kolvarna.si
Some of the basic requirements:

1.) Logo must basicly stay the same, it could only be a little "modernised".
2.) Main goal is to generate more sales, so webpage must be much more sales oriented.
3.) Focus is on category page and product page. Those two page types must be realy designed very well
4.) Mobile first, there are 80% customers over mobile devices
5.) Mobile menu must be also much better
6.) Category description will go under listed products
7.) On product page, there must be much bigger product images, and also mobile friendly image slider
8.) Big add to cart buttons
9.) Badges about safe shopping, possible returning goods, 100% warranty
10.) exposed product videos, images between text
11.) cleary exposed product benefits
11.) Products, which have sizes to choose, must have more user friendly choose option
12.) category page on desktop can have only products in all width, not side menu on the left
13.) Exposed CTA's on product page

You can create this category page: https://kolvarna.si/posteljnina
You can create this product page: https://kolvarna.si/oblikovalni-pas-brinel-hlacke

In short: mobile first, very sales oriented, look like 2018, big images, great shopping experience.

Target Market(s)

6 European coutries

Industry/Entity Type

E-Commerce

Number of Pages Required

3 page

Font styles to use
Sans Serif

Colors

Designer to choose colors to be used in the design.

Requirements
Must have
• Mobile first design
• Big images
• Very sales oriented
• CTA's through product description
Nice to have
• Product badges, like for example "100% cotton", "On stock", "Sale", "New"
Should not have
• Should not be copied from somewhere.

```html
<!DOCTYPE html>
<html lang="en">
<head>
<meta charset="utf-8">
<title>Kolvarna – Home</title>
<link href="https://fonts.googleapis.com/css2?family=Lato:wght@400;700;900&display=swap" rel="stylesheet">
<style>
:root{
  --orange:#f7a936;
  --blue:#1a9fd4;
  --dark:#333333;
  --text:#444444;
  --muted:#777777;
  --line:#dddddd;
  --soft:#f3f3f3;
  --red:#e0323a;
  --purple:#a23fd6;
  --green:#2fd66a;
  --sky:#2a8fd6;
}
*{box-sizing:border-box;margin:0;padding:0}
html,body{width:1200px;height:2624px;overflow:hidden;background:#fff;font-family:"Lato",sans-serif;color:var(--text)}
.page{position:relative;width:1200px;height:2624px}
.abs{position:absolute}
svg{display:block}

.topbar{left:0;top:0;width:1200px;height:56px;background:var(--dark);color:#fff;font-size:12px;font-weight:700}
.topbar .currency{position:absolute;left:73px;top:21px}
.topbar .contact{position:absolute;top:19px;display:flex;align-items:center;gap:10px;font-size:13px}

.header{left:0;top:56px;width:1200px;height:110px;background:#fafafa}
.brand{position:absolute;left:73px;top:33px;display:flex;align-items:center;gap:10px}
.brand-dot{width:44px;height:44px;border-radius:50%;background:var(--orange)}
.brand-name{font-size:22px;font-weight:900;color:var(--orange);letter-spacing:.5px}
.search{position:absolute;left:647px;top:32px;width:262px;height:45px;border-radius:23px;background:#fff;box-shadow:0 1px 4px rgba(0,0,0,.06);font-size:13px;color:#aaa;padding:14px 0 0 26px}
.search svg{position:absolute;right:18px;top:13px}
.icon-btn{position:absolute;top:32px;width:46px;height:46px;border-radius:50%;border:1px solid #ccc;background:#fff;display:flex;align-items:center;justify-content:center}
.cart-count{position:absolute;right:-6px;top:-8px;width:20px;height:20px;border-radius:50%;background:var(--orange);color:#fff;font-size:11px;display:flex;align-items:center;justify-content:center}

.nav{left:0;top:190px;width:1200px;display:flex;justify-content:center;gap:22px;font-size:13px;color:var(--dark);text-transform:uppercase}
.nav span{display:flex;align-items:center;gap:4px}
.rule{height:1px;background:var(--line)}

.social{left:0;width:44px;height:38px;background:var(--sky)}
.social.ig{background:var(--orange)}

.hero-main{left:73px;top:264px;width:627px;height:329px;background:linear-gradient(135deg,#6b6b6b,#c9c6c0 55%,#8a857d);display:flex;flex-direction:column;align-items:center;justify-content:center;gap:26px}
.hero-main p{color:#fff;font-size:18px}
.btn-orange{background:var(--orange);color:#fff;font-size:14px;text-transform:uppercase;border-radius:22px;padding:13px 36px}
.hero-side{left:722px;width:403px;display:flex;align-items:flex-end;padding:0 0 16px 14px;color:#fff;font-size:18px}
.hero-side.gift{top:264px;height:165px;background:linear-gradient(135deg,#7e8a98,#5a6676)}
.hero-side.kids{top:451px;height:142px;background:linear-gradient(135deg,#c9a7c6,#a9bfd0)}

.section-title{left:0;width:1200px;text-align:center;font-size:26px;font-weight:700;color:var(--dark);text-transform:uppercase}
.section-title em{font-style:normal;color:var(--orange)}

.tab{top:722px;height:48px;border:1px solid #ccc;font-size:14px;color:var(--dark);display:flex;align-items:center;justify-content:center}
.tab.active{background:var(--blue);border-color:var(--blue);color:#fff}

.card{width:259px;height:320px;border:1px solid #ccc;background:#fff;overflow:hidden}
.card .photo{position:absolute;left:50px;top:28px;width:158px;height:190px;border-radius:8px}
.card .photo.ph-watch{left:52px;top:38px;width:155px;height:155px;border-radius:50%}
.card .tag{position:absolute;left:0;top:210px;height:28px;padding:0 14px;background:var(--orange);color:#fff;font-size:11px;display:flex;align-items:center}
.card .divider{position:absolute;left:0;top:238px;width:100%;height:1px;background:var(--line)}
.card .name{position:absolute;left:0;top:256px;width:100%;text-align:center;font-size:13px;color:var(--text)}
.card .price{position:absolute;left:0;top:283px;width:100%;text-align:center;font-size:13px;color:var(--dark)}
.card .price s{color:#888;margin-right:8px}
.card .price b{font-weight:400;color:var(--blue)}
.ph-yellow{background:linear-gradient(135deg,#f6d84a,#e88f3a)}
.ph-green{background:linear-gradient(135deg,#6fc7e6,#5dbb5a)}
.ph-teal{background:linear-gradient(135deg,#3dc0d8,#2b8fb5)}
.ph-watch{background:radial-gradient(circle,#2a2a2a 60%,#111 100%)}

.arrow{width:36px;height:36px;border-radius:50%;background:#9a9a9a;display:flex;align-items:center;justify-content:center}

.promise{top:1170px;width:301px;height:75px;background:#f5f5f5;display:flex;align-items:center;justify-content:center;gap:14px;font-size:15px;color:var(--dark)}
.promise.red{border-top:3px solid var(--red)}
.promise.purple{border-top:3px solid var(--purple)}
.promise.green{border-top:3px solid var(--green)}

.faded{position:absolute;inset:0;background:rgba(255,255,255,.72)}
.quick{position:absolute;top:112px;width:40px;height:40px;border-radius:50%;background:#fff;border:1px solid #aaa;display:flex;align-items:center;justify-content:center}
.countdown{position:absolute;left:44px;top:120px;width:172px;display:flex;justify-content:space-between;color:var(--dark);font-size:13px;text-align:center}
.countdown div{background:rgba(255,255,255,.85);padding:3px 5px;line-height:1.6;min-width:34px}

.feature{top:1723px;width:196px;height:154px;background:#f5f5f5;text-align:center}
.feature .ring{position:absolute;left:68px;top:-6px;width:60px;height:60px;border-radius:50%;background:#f5f5f5;display:flex;align-items:center;justify-content:center}
.feature h4{position:absolute;left:0;top:85px;width:100%;font-size:15px;font-weight:400;color:var(--dark)}
.feature p{position:absolute;left:0;top:111px;width:100%;font-size:11px;color:var(--text)}
.feature .bar{position:absolute;left:0;bottom:0;width:100%;height:3px}

.posts{left:0;top:1929px;width:1200px;height:450px;background:var(--soft)}
.date{left:159px;top:2067px;width:75px;height:84px;border:1px solid #9fd1ea;background:#fff;text-align:center}
.date .day{height:40px;background:var(--blue);color:#fff;font-size:22px;padding-top:7px}
.date .mon{font-size:19px;padding-top:10px;color:var(--dark)}
.post-photo{left:252px;top:2067px;width:250px;height:219px;background:linear-gradient(180deg,#9cbbd6 0%,#c7d7e2 50%,#a89b63 75%,#8a7d4a 100%)}
.post-title{left:519px;top:2074px;font-size:22px;color:var(--dark)}
.post-by{left:524px;top:2113px;font-size:14px;color:var(--text)}
.post-by span{color:var(--orange)}
.post-text{left:519px;top:2145px;width:545px;font-size:14px;line-height:27px;color:var(--text)}
.btn-blue{left:519px;top:2246px;width:137px;height:42px;background:var(--blue);color:#fff;font-size:14px;display:flex;align-items:center;justify-content:center;text-transform:uppercase}

.footer{left:0;top:2379px;width:1200px;height:245px;background:var(--dark);color:#fff}
.footer h5{position:absolute;font-size:17px;font-weight:700}
.footer ul{position:absolute;list-style:none;font-size:13px;line-height:27px}
.footer .seal{position:absolute}
.footer .hr{position:absolute;left:110px;top:178px;width:980px;height:1px;background:#555}
.footer .copy{position:absolute;left:110px;top:201px;font-size:13px}
.footer .pay{position:absolute;top:199px;font-size:17px;font-weight:900;color:#4a74c9}
</style>
</head>
<body>
<div class="page">

  <div class="abs topbar">
    <span class="currency">USD</span>
    <span class="contact" style="left:840px">
      <svg width="16" height="16" viewBox="0 0 24 24"><path d="M6.6 10.8a15 15 0 0 0 6.6 6.6l2.2-2.2a1 1 0 0 1 1-.25 11 11 0 0 0 3.6.6 1 1 0 0 1 1 1V20a1 1 0 0 1-1 1A17 17 0 0 1 3 4a1 1 0 0 1 1-1h3.5a1 1 0 0 1 1 1 11 11 0 0 0 .6 3.6 1 1 0 0 1-.25 1z" fill="#fff"/></svg>
      013-5550182
    </span>
    <span class="contact" style="left:983px">
      <svg width="22" height="16" viewBox="0 0 22 16"><rect x="1" y="1" width="20" height="14" fill="none" stroke="#fff" stroke-width="1.6"/><path d="M1 1l10 8 10-8M1 15l7-6M21 15l-7-6" fill="none" stroke="#fff" stroke-width="1.6"/></svg>
      info@kolvarna.si
    </span>
  </div>

  <div class="abs header">
    <div class="brand"><div class="brand-dot"></div><span class="brand-name">KOLVARNA</span></div>
    <div class="search">Search
      <svg width="18" height="18" viewBox="0 0 20 20"><circle cx="8" cy="8" r="6" fill="none" stroke="#222" stroke-width="2.4"/><path d="M12.5 12.5L18 18" stroke="#222" stroke-width="2.6"/></svg>
    </div>
    <div class="icon-btn" style="left:939px"><svg width="16" height="15" viewBox="0 0 24 22"><path d="M12 20S2 13.5 2 7a5 5 0 0 1 10-1 5 5 0 0 1 10 1c0 6.5-10 13-10 13z" fill="none" stroke="#333" stroke-width="1.8"/></svg></div>
    <div class="icon-btn" style="left:1005px"><svg width="14" height="16" viewBox="0 0 20 22"><circle cx="10" cy="6" r="4.5" fill="none" stroke="#333" stroke-width="1.8"/><path d="M2 21a8 8 0 0 1 16 0" fill="none" stroke="#333" stroke-width="1.8"/></svg></div>
    <div class="icon-btn" style="left:1070px"><svg width="16" height="15" viewBox="0 0 24 22"><path d="M1 2h4l3 12h12l3-9H7" fill="none" stroke="#333" stroke-width="1.8"/><circle cx="10" cy="19" r="1.6" fill="#333"/><circle cx="18" cy="19" r="1.6" fill="#333"/></svg><span class="cart-count">0</span></div>
  </div>

  <nav class="abs nav">
    <span>Home and stay <svg width="10" height="6" viewBox="0 0 10 6"><path d="M1 1l4 4 4-4" fill="none" stroke="#f7a936" stroke-width="1.4"/></svg></span>
    <span>Bedding <svg width="10" height="6" viewBox="0 0 10 6"><path d="M1 1l4 4 4-4" fill="none" stroke="#f7a936" stroke-width="1.4"/></svg></span>
    <span>Children <svg width="10" height="6" viewBox="0 0 10 6"><path d="M1 1l4 4 4-4" fill="none" stroke="#f7a936" stroke-width="1.4"/></svg></span>
    <span>Beauty <svg width="10" height="6" viewBox="0 0 10 6"><path d="M1 1l4 4 4-4" fill="none" stroke="#f7a936" stroke-width="1.4"/></svg></span>
    <span>Dekor <svg width="10" height="6" viewBox="0 0 10 6"><path d="M1 1l4 4 4-4" fill="none" stroke="#f7a936" stroke-width="1.4"/></svg></span>
    <span>Presents <svg width="10" height="6" viewBox="0 0 10 6"><path d="M1 1l4 4 4-4" fill="none" stroke="#f7a936" stroke-width="1.4"/></svg></span>
    <span>Picnic &amp; party <svg width="10" height="6" viewBox="0 0 10 6"><path d="M1 1l4 4 4-4" fill="none" stroke="#f7a936" stroke-width="1.4"/></svg></span>
    <span>Discounts <svg width="10" height="6" viewBox="0 0 10 6"><path d="M1 1l4 4 4-4" fill="none" stroke="#f7a936" stroke-width="1.4"/></svg></span>
    <span>Outlet</span>
  </nav>
  <div class="abs rule" style="left:73px;top:240px;width:1052px"></div>

  <div class="abs social" style="top:370px"></div>
  <div class="abs social ig" style="top:412px"></div>

  <div class="abs hero-main" role="img" aria-label="Bright living room interior with plant and sofa">
    <p>Home and garden products, collected in one place.</p>
    <span class="btn-orange">Find more</span>
  </div>
  <div class="abs hero-side gift" role="img" aria-label="Wrapped gift boxes">Lorem ipsum dolor sit amet.</div>
  <div class="abs hero-side kids" role="img" aria-label="Children's bedding with cartoon toy pattern">Lorem ipsum dolor sit amet.</div>
  <div class="abs rule" style="left:73px;top:623px;width:1052px"></div>

  <h2 class="abs section-title" style="top:658px"><em>Latest</em> products</h2>

  <div class="abs tab active" style="left:73px;width:114px">New</div>
  <div class="abs tab" style="left:208px;width:126px">Selling Shit</div>
  <div class="abs tab" style="left:357px;width:136px">Special Offer</div>
  <div class="abs tab" style="left:516px;width:150px">Most viewed</div>

  <div class="abs card" style="left:73px;top:794px">
    <div class="photo ph-yellow" role="img" aria-label="Children's bedding set with cartoon print"></div>
    <div class="divider"></div>
    <div class="name">Baby bedding Snow sisters forever</div>
    <div class="price">$150.00v</div>
  </div>
  <div class="abs card" style="left:338px;top:794px">
    <div class="photo ph-green" role="img" aria-label="Children's bedding set with playful cartoon print"></div>
    <div class="tag">NEW</div><div class="divider"></div>
    <div class="name">Baby bedding Snow sisters forever</div>
    <div class="price">$150.00v</div>
  </div>
  <div class="abs card" style="left:602px;top:794px">
    <div class="photo ph-teal" role="img" aria-label="Children's bedding set with winter princess print"></div>
    <div class="tag">8% OFF</div><div class="divider"></div>
    <div class="name">Baby bedding Snow sisters forever</div>
    <div class="price"><s>$150.00</s>– <b>$120.00</b></div>
  </div>
  <div class="abs card" style="left:866px;top:794px">
    <div class="photo ph-watch" role="img" aria-label="Black smartwatch"></div>
    <div class="tag">NEW</div><div class="divider"></div>
    <div class="name">Baby bedding Snow sisters forever</div>
    <div class="price">$150.00v</div>
  </div>
  <div class="abs arrow" style="left:54px;top:923px"><svg width="8" height="12" viewBox="0 0 8 12"><path d="M6 1L1 6l5 5" fill="none" stroke="#fff" stroke-width="1.5"/></svg></div>
  <div class="abs arrow" style="left:1100px;top:923px"><svg width="8" height="12" viewBox="0 0 8 12"><path d="M2 1l5 5-5 5" fill="none" stroke="#fff" stroke-width="1.5"/></svg></div>

  <div class="abs promise red" style="left:101px">
    <svg width="40" height="34" viewBox="0 0 40 34"><path d="M6 8h28v24H6z M2 8h36" fill="none" stroke="#222" stroke-width="1.8"/><path d="M13 8V5a7 4 0 0 1 14 0v3M14 16a6 6 0 0 0 12 0" fill="none" stroke="#222" stroke-width="1.8"/></svg>
    100% Safe Shopping
  </div>
  <div class="abs promise purple" style="left:449px">
    <svg width="36" height="34" viewBox="0 0 36 34"><path d="M3 15h7v17H3zM10 16l7-13a3 3 0 0 1 5 2l-2 9h11a3 3 0 0 1 3 3l-3 12a3 3 0 0 1-3 3H10" fill="none" stroke="#222" stroke-width="1.8"/></svg>
    Possible Returning Goods
  </div>
  <div class="abs promise green" style="left:799px">
    <svg width="38" height="36" viewBox="0 0 38 36"><circle cx="19" cy="14" r="11" fill="none" stroke="#222" stroke-width="1.8"/><path d="M19 8l2 4 4.4.6-3.2 3 .8 4.4-4-2.1-4 2.1.8-4.4-3.2-3 4.4-.6z" fill="none" stroke="#222" stroke-width="1.5"/><path d="M11 23L6 33l6-2 3 4 3-9M27 23l5 10-6-2-3 4-3-9" fill="none" stroke="#222" stroke-width="1.6"/></svg>
    100% Warranty
  </div>

  <h2 class="abs section-title" style="top:1296px"><em>Gift</em> program</h2>

  <div class="abs card" style="left:73px;top:1362px;border-color:#eee;box-shadow:0 4px 14px rgba(0,0,0,.08)">
    <div class="photo ph-yellow" role="img" aria-label="Children's bedding set with cartoon print"></div>
    <div class="faded"></div>
    <div class="quick" style="left:80px"><svg width="16" height="15" viewBox="0 0 24 22"><path d="M12 20S2 13.5 2 7a5 5 0 0 1 10-1 5 5 0 0 1 10 1c0 6.5-10 13-10 13z" fill="none" stroke="#333" stroke-width="1.8"/></svg></div>
    <div class="quick" style="left:134px"><svg width="16" height="15" viewBox="0 0 24 22"><path d="M1 2h4l3 12h12l3-9H7" fill="none" stroke="#333" stroke-width="1.8"/><circle cx="10" cy="19" r="1.6" fill="#333"/><circle cx="18" cy="19" r="1.6" fill="#333"/></svg></div>
    <svg style="position:absolute;left:46px;top:174px" width="22" height="22" viewBox="0 0 22 22"><path d="M20 2L2 10l8 2 2 8z" fill="none" stroke="#222" stroke-width="1.6"/></svg>
    <div class="name" style="color:#aaa">Baby bedding Snow sisters forever</div>
    <div class="price" style="color:#aaa">$150.00v</div>
  </div>
  <div class="abs card" style="left:338px;top:1362px">
    <div class="photo ph-green" role="img" aria-label="Children's bedding set with playful cartoon print"></div>
    <div class="tag">NEW</div><div class="divider"></div>
    <div class="name">Baby bedding Snow sisters forever</div>
    <div class="price">$150.00v</div>
  </div>
  <div class="abs card" style="left:602px;top:1362px">
    <div class="photo ph-teal" role="img" aria-label="Children's bedding set with winter princess print"></div>
    <div class="countdown"><div>44<br>days</div><div>09<br>hours</div><div>22<br>min</div><div>34<br>sec</div></div>
    <div class="tag">8% OFF</div><div class="divider"></div>
    <div class="name">Baby bedding Snow sisters forever</div>
    <div class="price"><s>$150.00</s>– <b>$120.00</b></div>
  </div>
  <div class="abs card" style="left:866px;top:1362px">
    <div class="photo ph-watch" role="img" aria-label="Black smartwatch"></div>
    <div class="tag">NEW</div><div class="divider"></div>
    <div class="name">Baby bedding Snow sisters forever</div>
    <div class="price">$150.00v</div>
  </div>
  <div class="abs arrow" style="left:54px;top:1493px"><svg width="8" height="12" viewBox="0 0 8 12"><path d="M6 1L1 6l5 5" fill="none" stroke="#fff" stroke-width="1.5"/></svg></div>
  <div class="abs arrow" style="left:1100px;top:1493px"><svg width="8" height="12" viewBox="0 0 8 12"><path d="M2 1l5 5-5 5" fill="none" stroke="#fff" stroke-width="1.5"/></svg></div>

  <div class="abs feature" style="left:131px">
    <div class="ring"><svg width="34" height="26" viewBox="0 0 34 26"><path d="M2 3h20v16H2zM22 9h6l4 5v5H22" fill="none" stroke="#222" stroke-width="1.6"/><circle cx="8" cy="21" r="3" fill="#f5f5f5" stroke="#222" stroke-width="1.6"/><circle cx="27" cy="21" r="3" fill="#f5f5f5" stroke="#222" stroke-width="1.6"/></svg></div>
    <h4>Quick Delivery</h4><p>Throughout Slovenia only € 3.60</p>
    <div class="bar" style="background:var(--red)"></div>
  </div>
  <div class="abs feature" style="left:378px">
    <div class="ring"><svg width="30" height="32" viewBox="0 0 30 32"><path d="M15 6a8 8 0 0 0-5 14v4h10v-4a8 8 0 0 0-5-14zM11 28h8" fill="none" stroke="#222" stroke-width="1.6"/><path d="M15 1v2M3 12h2M25 12h2M6 4l1.5 1.5M24 4l-1.5 1.5" stroke="#222" stroke-width="1.6"/></svg></div>
    <h4>Support</h4><p>Throughout Slovenia only € 3.60</p>
    <div class="bar" style="background:var(--purple)"></div>
  </div>
  <div class="abs feature" style="left:624px">
    <div class="ring"><svg width="28" height="28" viewBox="0 0 28 28"><path d="M3 14V3h11l12 12-11 11z" fill="none" stroke="#222" stroke-width="1.6"/><circle cx="9" cy="9" r="2" fill="#222"/><path d="M10 16l6-6M13 19l6-6" stroke="#222" stroke-width="1.4"/></svg></div>
    <h4>Terms of payment</h4><p>Throughout Slovenia only € 3.60</p>
    <div class="bar" style="background:var(--green)"></div>
  </div>
  <div class="abs feature" style="left:873px">
    <div class="ring"><svg width="26" height="30" viewBox="0 0 26 30"><path d="M13 2l10 4v8c0 7-5 12-10 14C8 26 3 21 3 14V6z" fill="none" stroke="#222" stroke-width="1.6"/><circle cx="13" cy="14" r="5" fill="none" stroke="#222" stroke-width="1.6"/><path d="M10.5 14l2 2 3-3.5" fill="none" stroke="#222" stroke-width="1.5"/></svg></div>
    <h4>Secure purchases</h4><p>Throughout Slovenia only € 3.60</p>
    <div class="bar" style="background:var(--sky)"></div>
  </div>

  <div class="abs posts"></div>
  <h2 class="abs section-title" style="top:1978px"><em>New</em> posts</h2>
  <div class="abs arrow" style="left:59px;top:2159px"><svg width="8" height="12" viewBox="0 0 8 12"><path d="M6 1L1 6l5 5" fill="none" stroke="#fff" stroke-width="1.5"/></svg></div>
  <div class="abs arrow" style="left:1101px;top:2159px"><svg width="8" height="12" viewBox="0 0 8 12"><path d="M2 1l5 5-5 5" fill="none" stroke="#fff" stroke-width="1.5"/></svg></div>
  <div class="abs date"><div class="day">16</div><div class="mon">Nov</div></div>
  <div class="abs post-photo" role="img" aria-label="Traveller with a suitcase on a country road under a blue sky"></div>
  <h3 class="abs post-title" style="font-weight:400">Travel with bedding around the world</h3>
  <div class="abs post-by">By <span>Admin</span></div>
  <p class="abs post-text">Perhaps this year did not come out and the holidays were not exactly what you wanted. We allow you to travel around the world with us. You can also end up on the other end of the day. ...</p>
  <div class="abs btn-blue">Read more</div>

  <footer class="abs footer">
    <h5 style="left:110px;top:35px">Informations</h5>
    <ul style="left:110px;top:66px"><li>About us</li><li>Delivery Information</li><li>Terms of Business</li></ul>
    <ul style="left:338px;top:34px"><li>Protection of personal Data</li><li>Product return Policy</li><li>Wholesale B2B</li><li>FAQ - FAQ</li><li>Affiliate Program</li></ul>
    <h5 style="left:635px;top:37px;font-size:15px">Customer Service</h5>
    <ul style="left:632px;top:66px"><li>Contact</li><li>Sitemap</li><li>Gift Certificates</li></ul>
    <div class="seal" style="left:840px;top:30px;width:110px;height:50px;border-radius:8px;background:var(--orange)"></div>
    <div class="seal" style="left:840px;top:94px;width:120px;height:60px;border-radius:8px;background:#8a8a8a"></div>
    <div class="seal" style="left:1002px;top:30px;width:70px;height:70px;border-radius:50%;background:#e8b93a"></div>
    <div class="hr"></div>
    <div class="copy">Kolvarna.si @ 2018</div>
    <div class="pay" style="left:835px">Cardimo</div>
    <div class="pay" style="left:930px;color:#3a8fd9">Walnetta</div>
  </footer>

</div>
</body>
</html>
```